TOWNHAX3 Research Outcomes (e-Toolkit)

I would like you to design an electronic document that can be used to display the outcomes of the TOWNHAX3 Research that can easily be downloaded from a website. This document will help nurses, educators, students and their supervisors to be able to better understand the outcomes of the research and apply it to their own practice. It should be something they can print out (A4 size) and refer to easily. It should be quite graphical and represent male and female nurses working in different specialty areas (emergency, primary healthcare, aged care, etc.), across hospital to primary healthcare (community) contexts. It should be professional, clean and crisp in appearance. There are areas in yellow in the attached document that are yet to be determined. All images within the document can be amended to better reflect the design of the document and the intent of its contained content. An example of the type of document I'm looking for is attached as "standards.pdf". It should be approximately 15 pages in length.
Updates

The project does not have to use the TOWNHAX3 logo or its colours as a main design feature of the project.

Target Market(s)

Nurses, educators and students.

Industry/Entity Type

Education

Font styles to use
Sans Serif

Colors

Designer to choose colors to be used in the design.

Requirements
Must have
• Must have a diagram depicting the interrelatedness of all the individual metaspecialties. The contained diagrams can be modified to suit graphic design needs.
• Images of nursing professionals should appear Australian.
Nice to have
• I would like them to try and re-configure the diagrams as they are boring and I hate the colours. Images of collaboration amongst different healthcare team members would be nice.
Should not have
• Only images of female nurses or only images (if chosen) of nurses only working in a hospital.

```html
<!DOCTYPE html>
<html lang="en">
<head>
<meta charset="utf-8">
<title>TOWNHAX3 Toolkit – Section 1: Introduction</title>
<link href="https://fonts.googleapis.com/css2?family=Roboto+Condensed:wght@300;400;700&display=swap" rel="stylesheet">
<style>
  :root {
    --green: #45c476;
    --purple: #5a1fa6;
    --ink: #1e1e1e;
    --white: #ffffff;
  }
  * { box-sizing: border-box; margin: 0; padding: 0; }
  html, body { width: 848px; height: 1200px; overflow: hidden; background: var(--white); }
  .page {
    position: relative;
    width: 848px;
    height: 1200px;
    overflow: hidden;
    font-family: "Roboto Condensed", "Arial Narrow", sans-serif;
    color: var(--ink);
    background: var(--white);
  }
  .page-header { position: absolute; top: 0; left: 0; width: 848px; height: 107px; }
  .page-header svg { position: absolute; inset: 0; }
  .section-title {
    position: absolute;
    left: 26px;
    top: 36px;
    font-size: 29px;
    font-weight: 700;
    color: var(--white);
    letter-spacing: 0.3px;
  }
  .brand {
    position: absolute;
    right: 26px;
    top: 40px;
    display: flex;
    align-items: center;
    gap: 7px;
    font-size: 19px;
    font-weight: 700;
    color: var(--green);
  }
  .brand-mark { width: 14px; height: 14px; background: var(--purple); }
  .content {
    position: absolute;
    left: 43px;
    top: 162px;
    width: 762px;
    font-size: 15px;
    font-weight: 400;
    line-height: 21px;
    text-align: justify;
  }
  .content p { margin-bottom: 21px; }
  .content h2 {
    font-size: 20px;
    font-weight: 700;
    color: var(--purple);
    line-height: 26px;
    margin-bottom: 2px;
  }
  .content .tight { margin-bottom: 0; }
  .standards-list { list-style: none; margin: 0 0 21px 11px; }
  .page-footer { position: absolute; left: 0; bottom: 0; width: 848px; height: 60px; }
  .page-footer svg { position: absolute; inset: 0; }
  .page-number {
    position: absolute;
    left: 762px;
    top: 23px;
    font-size: 17px;
    font-weight: 400;
    color: var(--white);
  }
</style>
</head>
<body>
<div class="page">
  <header class="page-header">
    <svg width="848" height="107" viewBox="0 0 848 107" aria-hidden="true">
      <polygon points="0,0 670,0 640,107 0,107" fill="var(--green)"/>
      <polygon points="682,0 704,0 674,107 652,107" fill="var(--purple)"/>
    </svg>
    <h1 class="section-title">SECTION 1: INTRODUCTION</h1>
    <div class="brand"><span class="brand-mark"></span>TOWNHAX3</div>
  </header>

  <main class="content">
    <p>This research-based toolkit is one of the deliverables in a six-year research program exploring Australian nurse practitioner clinical learning, educational governance and capability. The program has been completed by a team of Australian nurse academics and clinicians in close collaboration with the National Guild of Advanced Nurses.</p>

    <h2>Overview</h2>
    <p class="tight">The nurse practitioner is a rapidly expanding clinical role in Australia, with specialty areas emerging originally through identification of unmet healthcare needs. The nurse practitioner title is protected by endorsement through the Nursing Practice Registration Council (NPRC). Preparation for the role is achieved through completion of an approved Master's Degree, as well as the demonstration of extensive clinical practice as a nurse working at an advanced level of practice. The degree programme is currently offered by approximately 15 Australian Universities. These university programs are accredited and approved by the NPRC to enable students to meet a set of nationally agreed professional standards and result in endorsement as a nurse practitioner. Once endorsed, nurse practitioners work across a diverse range of clinical specialty areas. One aim of the clinical learning, governance and capability (TOWNHAX3) study was to guide consistency of specialty clinical learning and teaching for these Masters' level nurse practitioner students. A broad specialty taxonomy was developed that comprises constructs termed 'metaspecialties'. Each metaspecialty is supported by clinical practice standards that exemplify its requisite advanced knowledge, skills and expertise. These metaspecialty clinical practice standards have been developed and validated through national research with nurse practitioners to guide clinical learning and teaching approaches that support the development of an advanced level of nursing practice required for the nurse practitioner role.</p>
    <p class="tight">The six sets of clinical practice standards are (in alphabetical order):</p>
    <ul class="standards-list">
      <li>Ageing and palliative care,</li>
      <li>Child and family health care,</li>
      <li>Chronic and complex care,</li>
      <li>Emergency and acute care,</li>
      <li>Mental health care,</li>
      <li>Primary health care.</li>
    </ul>
    <p>The standards for the emergency and acute care metaspecialty comprise both acute care standards developed as part of the TOWNHAX3 study and some standards selected from previous research by Dr Mara Ellison (Ellison, 2015), which used the same methodology to develop emergency nurse practitioner clinical practice standards. Dr Ellison advised and gave permission for these inclusions. The remainder of the toolkit describes how to use the toolkit and then provides descriptions of each metaspecialty followed by their respective standards.</p>
  </main>

  <footer class="page-footer">
    <svg width="848" height="60" viewBox="0 0 848 60" aria-hidden="true">
      <rect x="0" y="0" width="848" height="60" fill="var(--purple)"/>
      <polygon points="680,15 848,15 848,60 725,60" fill="var(--green)"/>
    </svg>
    <span class="page-number">page : 2</span>
  </footer>
</div>
</body>
</html>
```